Scientific project description

Here is a project description related to cellular mechanics, showing above the forces acting on cells in the tissues of our body. The forces on single cells are there to depict how forces are acting on cells (pressure squeezes the cell, shear flow is pushing the upward parts of the cell, tension pulls one part of the cell, strain is stretching the whole cell; the single cell images are to be found also on the last page). Intense red/purple are used to indicate that the forces are stressful (the colors to be used do not need to be exactly like these colors). The picture in the middle is a view of cells (same picture on next page if that needs to be modified). At the left, a description of what happens when everything is going well, i.e. the body stays healthy. At the right, if you dysfunction you get disease. Green nuances were used to indicate health, brownish, perhaps not so pleasant nuances were used to indicate disease. Below are the steps of the project.

On the whole, we're rather happy with the concept description as such, but it should look a little bit nicer. To many color nuances give a "noisy" impression, fonts could be nicer, layout more crisp, and the text on the steps should be more readable. We would also like to have two versions of the same picture, one with black background, one with white.

Target Market(s)

Scientists that are evaluating our project

Requirements
Must have
• Easy to grasp the idea, easy to read and understand the underlying idea.
Nice to have
• Would be good to have the Concept title ("Vorlix Concept and Envisioned Project Progression) on top of the figure as indicated in the second brief picture submitted.

```html
<!DOCTYPE html>
<html lang="en">
<head>
<meta charset="utf-8">
<title>Mechanostasis Concept</title>
<link href="https://fonts.googleapis.com/css2?family=PT+Sans&family=Share+Tech&display=swap" rel="stylesheet">
<style>
  :root {
    --bg: #0b0b0b;
    --health: #3dbb87;
    --disease: #e25430;
    --steps: #13767b;
    --text: #ffffff;
  }
  html, body {
    margin: 0;
    padding: 0;
    width: 1200px;
    height: 857px;
    overflow: hidden;
    background: var(--bg);
  }
  .concept {
    display: block;
    width: 1200px;
    height: 857px;
  }
  .label, .node-text, .steps-text {
    font-family: "PT Sans", sans-serif;
    fill: var(--text);
    text-anchor: middle;
  }
  .label { font-size: 22px; }
  .node-text { font-size: 24px; }
  .steps-text { font-size: 19px; }
  .core-title {
    font-family: "Share Tech", sans-serif;
    font-size: 35px;
    letter-spacing: 2.5px;
    fill: var(--text);
    text-anchor: middle;
  }
  .link-health { stroke: var(--health); stroke-width: 3; }
  .link-disease { stroke: var(--disease); stroke-width: 3; }
  .force { fill: var(--health); }
  .node-health { fill: var(--health); }
  .node-disease { fill: var(--disease); }
  .core-ring { fill: none; stroke: var(--health); stroke-width: 14; }
  .steps-box { fill: var(--steps); }
</style>
</head>
<body>
<svg class="concept" viewBox="0 0 1200 857" xmlns="http://www.w3.org/2000/svg">
  <rect width="1200" height="857" fill="var(--bg)"/>

  <!-- force connectors -->
  <g class="force-links">
    <line class="link-health" x1="339" y1="207" x2="427" y2="298"/>
    <line class="link-health" x1="503" y1="202" x2="512" y2="233"/>
    <line class="link-health" x1="674" y1="202" x2="666" y2="233"/>
    <line class="link-health" x1="832" y1="207" x2="743" y2="298"/>
  </g>

  <!-- mechanical forces -->
  <g class="forces">
    <text class="label" x="302" y="70">Pressure</text>
    <circle class="force" cx="304" cy="147" r="60" role="img" aria-label="Cell squeezed from above by pressure"/>

    <text class="label" x="499" y="51">Shear</text>
    <circle class="force" cx="496" cy="131" r="60" role="img" aria-label="Cell pushed sideways by shear flow"/>

    <text class="label" x="683" y="51">Tension</text>
    <circle class="force" cx="688" cy="131" r="60" role="img" aria-label="Cell pulled upward by tension"/>

    <text class="label" x="878" y="70">Strain</text>
    <circle class="force" cx="877" cy="147" r="60" role="img" aria-label="Cell stretched on both sides by strain"/>
  </g>

  <!-- core -->
  <g class="core">
    <circle class="core-ring" cx="588" cy="386" r="146"/>
    <text class="core-title" x="588" y="395">Mechanostasis</text>
  </g>

  <!-- health path -->
  <g class="health-path">
    <text class="label" x="358" y="359">Cell fitness</text>
    <line class="link-health" x1="306" y1="377" x2="405" y2="377"/>
    <circle class="node-health" cx="192" cy="377" r="95"/>
    <text class="node-text" x="193" y="355">Functional</text>
    <text class="node-text" x="193" y="386">cellular</text>
    <text class="node-text" x="193" y="417">machineries</text>
    <line class="link-health" x1="226" y1="478" x2="240" y2="504"/>
    <circle class="node-health" cx="276" cy="575" r="66"/>
    <text class="node-text" x="276" y="583">Health</text>
  </g>

  <!-- disease path -->
  <g class="disease-path">
    <text class="label" x="817" y="359">Cell frailty</text>
    <line class="link-disease" x1="764" y1="377" x2="864" y2="377"/>
    <circle class="node-disease" cx="988" cy="377" r="95"/>
    <text class="node-text" x="991" y="355">Dysfunctional</text>
    <text class="node-text" x="991" y="386">cellular</text>
    <text class="node-text" x="991" y="417">machineries</text>
    <line class="link-disease" x1="951" y1="478" x2="938" y2="504"/>
    <circle class="node-disease" cx="911" cy="575" r="66"/>
    <text class="node-text" x="912" y="583">Disease</text>
  </g>

  <!-- project steps -->
  <g class="steps">
    <rect class="steps-box" x="411" y="573" width="363" height="243" rx="38"/>
    <text class="steps-text" x="590" y="611">Therapies</text>
    <text class="steps-text" x="590" y="642">Prevention</text>
    <text class="steps-text" x="590" y="673">Critical targets</text>
    <text class="steps-text" x="590" y="704">Cellular machineries</text>
    <text class="steps-text" x="590" y="735">Disease models</text>
    <text class="steps-text" x="590" y="766">Cell, tissue &amp; organ responses</text>
    <text class="steps-text" x="590" y="797">Mechanical force models</text>
  </g>
</svg>
</body>
</html>
```